Emerging Australian photographer

I'm based in Cunderdin, a small rural town in the Wheatbelt area of Western Australia. So its a good thing that I love to travel further afield both for pleasure and for work. To me that is one and the same thing in any event!

My desire is to take photos that make the viewers heart skip. I love taking photos of people doing the things they love or being with the people they love. For me, the joy of photography comes with capturing the 'moments between the moments'. I like candid photography best of all - like when the new husband is staring joyfully at his bride and at that minute is unaware of the photographer capturing the moment.

I am available for weddings, engagements, birthdays, special events, newborns, family or individual portraits. By the end of the year I will be accredited with the Coastal Guild of Image Artisans.

I need a card that stands out but is elegant and would sit well on the table at a wedding or be given out in the church grounds. Classy and a little bit sassy.

Target Market(s)

Consumers who are seeking photographic services, eg wedding guests who see me at work and make enquiries.

Industry/Entity Type

Church

Contact Information for Business Card

Tamsin Bexley Photography
Tamsin Bexley
0452 307 618
www.tamsinbexley.com.au
photos@tamsinbexley.com.au

Requirements
Must have
• Must fit with the theme in the watermarks, but be crisp and modern.
Nice to have
• However it's not essential to have the pink! Facebook and Twitter logos.
Should not have
• Old style fonts like times new roman.

```html
<!DOCTYPE html>
<html lang="en">
<head>
<meta charset="utf-8">
<title>Tamsin Bexley Photography – Business Card</title>
<link rel="stylesheet" href="https://fonts.googleapis.com/css2?family=Josefin+Sans:wght@300;400&family=Yanone+Kaffeesatz:wght@300&display=swap">
<style>
  :root {
    --page-bg: #e9e9e8;
    --card-bg: #444244;
    --card-band: #3c393c;
    --ornament-tone: #3a373a;
    --badge-tone: #4b494b;
    --cream: #f5efb6;
    --card-shadow: 0 6px 14px rgba(0, 0, 0, 0.35);
  }
  * { box-sizing: border-box; margin: 0; padding: 0; }
  html, body {
    width: 1200px;
    height: 927px;
    overflow: hidden;
    background: var(--page-bg);
  }
  .canvas {
    position: relative;
    width: 1200px;
    height: 927px;
  }
  .card {
    position: absolute;
    width: 573px;
    height: 354px;
    background: var(--card-bg);
    box-shadow: var(--card-shadow);
    overflow: hidden;
  }
  /* Front */
  .card--front { left: 170px; top: 96px; }
  .brand {
    position: absolute;
    inset: 0;
    display: flex;
    align-items: center;
    justify-content: center;
    gap: 14px;
  }
  .brand__mark {
    width: 18px;
    height: 18px;
    border-radius: 50%;
    background: var(--cream);
  }
  .brand__name {
    font-family: "Josefin Sans", sans-serif;
    font-weight: 300;
    font-size: 32px;
    letter-spacing: 0.5px;
    color: var(--cream);
  }
  /* Back */
  .card--back { left: 490px; top: 478px; }
  .ornament-band {
    position: absolute;
    left: 0;
    top: 177px;
    width: 340px;
    height: 60px;
    background: linear-gradient(to bottom, var(--card-bg), var(--ornament-tone));
  }
  .contact-panel {
    position: absolute;
    left: 0;
    top: 237px;
    width: 340px;
    height: 117px;
    background: var(--card-band);
  }
  .accreditation-badge {
    position: absolute;
    left: 322px;
    top: 136px;
    width: 270px;
    height: 270px;
    border-radius: 50%;
    background: var(--badge-tone);
  }
  .contact {
    position: absolute;
    left: 20px;
    top: 238px;
    color: var(--cream);
  }
  .contact__name {
    font-family: "Yanone Kaffeesatz", sans-serif;
    font-weight: 300;
    font-size: 36px;
    line-height: 1;
  }
  .contact__phone {
    font-family: "Josefin Sans", sans-serif;
    font-weight: 300;
    font-size: 22px;
    letter-spacing: 1px;
    margin-top: 6px;
  }
  .contact__line {
    font-family: "Josefin Sans", sans-serif;
    font-weight: 300;
    font-size: 14px;
    line-height: 1.3;
  }
</style>
</head>
<body>
  <main class="canvas">
    <section class="card card--front" aria-label="Business card front">
      <div class="brand">
        <span class="brand__mark"></span>
        <span class="brand__name">Tamsin Bexley Photography</span>
      </div>
    </section>

    <section class="card card--back" aria-label="Business card back">
      <div class="ornament-band" role="img" aria-label="Decorative band of swirling flourishes and small hearts"></div>
      <div class="contact-panel"></div>
      <div class="accreditation-badge" role="img" aria-label="Accreditation badge"></div>
      <div class="contact">
        <p class="contact__name">Tamsin Bexley</p>
        <p class="contact__phone">0452 307 618</p>
        <p class="contact__line">www.tamsinbexley.com.au</p>
        <p class="contact__line">photos@tamsinbexley.com.au</p>
      </div>
    </section>
  </main>
</body>
</html>
```